Talvora Companies Business Card Design

We need a new business card for our Private Equity Real Estate Development firm, “Talvora” and our EB-5 regional center “Mossgate Regional Center” on one card. We prefer a design that is simple, elegant, and represents the luxury products we design and build as well as the financial security and stability our successful history has produced. We are an industry leader in our field and 3rd generation family business that has evolved into an institutional quality investment platform. Considered design size is standard business card dimensions (3.5 x 2 inches with an additional 1/8 inch space for design elements or backgrounds that extend beyond the finished size of your piece.

Target Market(s)

• High net worth individuals
• Highly skilled technical workers and physicians in the US seeking investment-based immigration opportunities
• Sophisticated private equity investors
• Intermediary partners include domestic attorneys and investment brokers, as well as international agent networks
• US real estate developers

Industry/Entity Type

Finance

Contact Information for Business Card

(Providing placeholder info for personal information, please design for longer character spaces, longer names and addresses etc..)
• Logo for Talvora
• Logo for Mossgate Regional Center
• Full name: Dermot Talvora
• Job title: CEO
• Email address: dtalvora@talvoracompanies.com
• Cell phone number: +1.555.314.2786
• Office number +1.555.862.4071
• Office address: Quillfield Park 7, 4817 Vista Loma, San Ramon, CA.
• Website: www.talvoracompanies.com

Font styles to use
Serif
Sans Serif

Colors
ec1f27
ffffff
000000

Requirements
Must have
• • Logo for Talvora
• • Logo for Mossgate Regional Center
• - Use rounded corners
• (See .ai file included for logos)
Nice to have
• • Simple, elegant design
• • Aesthetically compatible with our website design (www.talvoracompanies.com)
• • Color palette including but not limited to white, black, and red (as per logos)
Should not have
• - Not too much red color
• - Do not stack both logos on top of each other

```html
<!DOCTYPE html>
<html lang="en">
<head>
<meta charset="utf-8">
<title>Talvora Companies Business Card</title>
<link href="https://fonts.googleapis.com/css2?family=Cinzel:wght@600&family=Open+Sans:wght@400&display=swap" rel="stylesheet">
<style>
  :root {
    --backdrop: #7e7e7e;
    --card-white: #ffffff;
    --brand-red: #a31b2f;
    --ink-dark: #2b2b2b;
    --card-black: #1c1d1f;
    --text-light: #f4eeee;
    --mark-grey: #bdbdbd;
  }
  * { box-sizing: border-box; margin: 0; padding: 0; }
  html, body { width: 1200px; height: 802px; overflow: hidden; }
  body { background: var(--backdrop); position: relative; font-family: "Open Sans", Arial, sans-serif; }

  .card { position: absolute; box-shadow: 0 3px 8px rgba(0,0,0,.35); overflow: hidden; }

  /* Front */
  .card-front { left: 204px; top: 383px; width: 442px; height: 265px; background: var(--card-white); }
  .front-brand { position: absolute; left: 0; right: 0; top: 54px; display: flex; justify-content: center; align-items: center; gap: 12px; }
  .brand-square { width: 34px; height: 34px; background: var(--ink-dark); }
  .brand-name { font-family: "Cinzel", Georgia, serif; font-weight: 600; font-size: 25px; color: var(--ink-dark); letter-spacing: .5px; }
  .contact-band { position: absolute; left: 0; right: 0; top: 131px; bottom: 0; background: var(--brand-red); }
  .band-tab { position: absolute; left: 28px; top: 130px; }

  .holder-name { position: absolute; left: 23px; top: 157px; font-family: "Cinzel", Georgia, serif; font-weight: 600; font-size: 17px; color: var(--text-light); letter-spacing: .3px; }
  .holder-title { position: absolute; left: 23px; top: 175px; font-size: 13px; color: var(--text-light); }
  .address { position: absolute; left: 23px; top: 198px; font-size: 12.5px; line-height: 16px; color: var(--text-light); }
  .contacts { position: absolute; right: 22px; top: 183px; list-style: none; font-size: 12.5px; line-height: 16px; color: var(--text-light); text-align: right; }
  .contacts li { display: flex; justify-content: flex-end; align-items: center; gap: 3px; }
  .contacts svg { width: 11px; height: 11px; flex: none; }

  /* Back */
  .card-back { left: 681px; top: 166px; width: 301px; height: 483px; background: var(--card-black); }
  .back-field { position: absolute; inset: 0; background: linear-gradient(180deg, #202124 0%, #1a1b1d 100%); }
  .back-brand { position: absolute; left: 28px; top: 404px; display: flex; align-items: center; gap: 12px; }
  .back-brand .brand-square { width: 40px; height: 40px; background: var(--mark-grey); }
  .back-brand .brand-name { color: var(--text-light); font-size: 17px; line-height: 1.15; }
</style>
</head>
<body>

<section class="card card-front" aria-label="Front of business card">
  <div class="front-brand">
    <span class="brand-square"></span>
    <span class="brand-name">TALVORA CAPITAL</span>
  </div>
  <div class="contact-band"></div>
  <svg class="band-tab" width="44" height="14" viewBox="0 0 44 14" aria-hidden="true">
    <polygon points="0,0 44,0 44,6 22,13 0,6" fill="#ffffff"/>
  </svg>

  <p class="holder-name">DERMOT TALVORA</p>
  <p class="holder-title">CEO</p>
  <p class="address">Quillfield Park 7<br>4817 Vista Loma<br>San Ramon, CA</p>

  <ul class="contacts">
    <li>+1.555.314.2786
      <svg viewBox="0 0 12 12" aria-hidden="true"><path d="M1 4 Q6 0 11 4 L9 5 L8 4 H4 L3 5 Z M3 6 H9 L10 11 H2 Z" fill="#f4eeee"/></svg>
    </li>
    <li>+1.555.862.4071
      <svg viewBox="0 0 12 12" aria-hidden="true"><rect x="3" y="0.5" width="6" height="11" rx="1" fill="none" stroke="#f4eeee" stroke-width="1.2"/><rect x="5" y="9" width="2" height="1" fill="#f4eeee"/></svg>
    </li>
    <li>dtalvora@talvoracompanies.com
      <svg viewBox="0 0 12 12" aria-hidden="true"><rect x="0.5" y="2.5" width="11" height="7" fill="#f4eeee"/><polyline points="0.5,2.5 6,7 11.5,2.5" fill="none" stroke="#a31b2f" stroke-width="1"/></svg>
    </li>
    <li>www.talvoracompanies.com
      <svg viewBox="0 0 12 12" aria-hidden="true"><circle cx="6" cy="6" r="5.5" fill="#f4eeee"/><ellipse cx="6" cy="6" rx="2.4" ry="5.3" fill="none" stroke="#a31b2f" stroke-width=".8"/><line x1="0.5" y1="6" x2="11.5" y2="6" stroke="#a31b2f" stroke-width=".8"/></svg>
    </li>
  </ul>
</section>

<section class="card card-back" aria-label="Back of business card">
  <div class="back-field" role="img" aria-label="Dark background with a faint repeating brand pattern"></div>
  <div class="back-brand">
    <span class="brand-square"></span>
    <span class="brand-name">MOSSGATE<br>REGIONAL CENTER</span>
  </div>
</section>

</body>
</html>
```